Business card for apparel company. Specializing in fishing and boating performance wear. Main company name is Marlowe Teal Company, LLC brand name for apparel is WAKEFIN. See website www.WakefinReefline.com I will attach some logos to consider.

```html
<!DOCTYPE html>
<html lang="en">
<head>
<meta charset="utf-8">
<title>Wakefin Business Card</title>
<link rel="stylesheet" href="https://fonts.googleapis.com/css2?family=Roboto:wght@400;500;700;900&display=swap">
<style>
  :root {
    --page-bg: #2b2d31;
    --card-white: #ffffff;
    --brand-blue: #0a6fe0;
    --brand-sky: #0aa0e6;
    --text-grey: #4a4a4a;
    --icon-blue: #1a9ae0;
  }
  * { box-sizing: border-box; margin: 0; padding: 0; }
  html, body {
    width: 1200px; height: 952px; overflow: hidden;
    background: var(--page-bg);
    font-family: "Roboto", Arial, sans-serif;
  }
  .stage { position: relative; width: 1200px; height: 952px; }
  .card {
    position: absolute; left: 320px; width: 560px; height: 320px;
    border-radius: 26px; overflow: hidden;
    box-shadow: 0 10px 30px rgba(0,0,0,.45);
  }
  .card-front { top: 100px; background: var(--card-white); }
  .card-back {
    top: 520px;
    background: linear-gradient(160deg, #0a6fe0 0%, #0a8ee6 55%, #0aa4ea 100%);
  }
  .wordmark {
    position: absolute; font-weight: 900; letter-spacing: 3px;
    font-size: 44px; line-height: 1;
  }
  .card-front .wordmark { left: 40px; top: 36px; color: var(--brand-blue); }
  .card-back .wordmark { left: 0; right: 0; top: 196px; text-align: center; color: var(--card-white); }
  .contact-list { position: absolute; left: 40px; top: 116px; list-style: none; }
  .contact-item {
    display: flex; align-items: flex-start; gap: 8px;
    font-size: 13px; color: var(--text-grey); line-height: 16px; margin-bottom: 7px;
  }
  .contact-icon { flex: 0 0 16px; width: 16px; height: 16px; }
  .holder { position: absolute; right: 40px; top: 120px; text-align: right; }
  .holder-name { font-size: 28px; font-weight: 700; color: var(--brand-blue); }
  .holder-title { font-size: 16px; color: var(--text-grey); margin-top: 2px; }
  .holder-rule { display: inline-block; width: 56px; height: 2px; background: var(--brand-blue); margin-top: 8px; }
  .pattern-field { position: absolute; inset: 0; }
</style>
</head>
<body>
<main class="stage">
  <section class="card card-front" aria-label="Card front">
    <div class="wordmark">WAKEFIN</div>
    <ul class="contact-list">
      <li class="contact-item">
        <svg class="contact-icon" viewBox="0 0 16 16"><rect width="16" height="16" rx="3" fill="var(--icon-blue)"/><path d="M8 3a3.5 3.5 0 0 0-3.5 3.5C4.5 9 8 13 8 13s3.5-4 3.5-6.5A3.5 3.5 0 0 0 8 3z" fill="#fff"/><circle cx="8" cy="6.5" r="1.3" fill="var(--icon-blue)"/></svg>
        <span>P.O. Box 418 Harborview<br>Florida 33720</span>
      </li>
      <li class="contact-item">
        <svg class="contact-icon" viewBox="0 0 16 16"><rect width="16" height="16" rx="3" fill="var(--icon-blue)"/><path d="M5 3.5l2 2-1 1.5c.7 1.4 1.6 2.3 3 3l1.5-1 2 2-1.2 1.5C8 12.3 3.7 8 3.5 5.2z" fill="#fff"/></svg>
        <span>555-010-4827</span>
      </li>
      <li class="contact-item">
        <svg class="contact-icon" viewBox="0 0 16 16"><rect width="16" height="16" rx="3" fill="var(--icon-blue)"/><rect x="3.5" y="5" width="9" height="6.5" fill="none" stroke="#fff" stroke-width="1.2"/><path d="M3.5 5l4.5 4 4.5-4" fill="none" stroke="#fff" stroke-width="1.2"/></svg>
        <span>info@MarloweTealCo.com</span>
      </li>
      <li class="contact-item">
        <svg class="contact-icon" viewBox="0 0 16 16"><rect width="16" height="16" rx="3" fill="var(--icon-blue)"/><path d="M5 4l6.5 4-3 .6-1.2 2.9z" fill="#fff"/></svg>
        <span>www.WakefinReefline.com</span>
      </li>
    </ul>
    <div class="holder">
      <div class="holder-name">Marlowe Teal</div>
      <div class="holder-title">CEO/Manger</div>
      <span class="holder-rule"></span>
    </div>
  </section>
  <section class="card card-back" aria-label="Card back">
    <div class="pattern-field" role="img" aria-label="Repeating brand pattern on blue"></div>
    <div class="wordmark">WAKEFIN</div>
  </section>
</main>
</body>
</html>
```